Need 2 sided card for Loomfield Goods Co. Logo supplied.

I am looking for a business card for my online craft supply business.

I have a very simple design already which I am kind of happy with (see attached pdf) - but would like suggestions for something a little more creative. Design MUST be clean. Super clean! Think thin lines and not blocks of color...

Design must be clean and crisp. No other colors other than in palette (see link below)

I would also like to possible incorporate my tagline - maybe on the front but definitely on the back:
"HollowReed Ideas & Hobby Materials"

Logo file is supplied, but I think spacing on the card may required the wording to be moved underneaths the camera icon - which is fine. Font in logo is Maven Pro. OPEN TO USE OF OTHER FONTS ON CARD BUT MUST BE CLEAN DESIGN.

FRONT OF CARD
All information on attached pdf is correct and should be shown in your design.

BACK OF CARD
Needs to show www.tindalerow.example and maybe logo repeat and tagline.

SIZE
New Zealand sized - meaning finished card will be 90 x 55mm
Printing requirements: printed area is 90mm x 55mm with a 2mm bleed all round.

COLORS
Color palette used in logo can be seen here for HEX and RGB reference: http://www.huebankly.example/palette/8627410/website

NOTE: PAYMENT WILL BE MADE FOR THE BEST DESIGN - EVEN IF I DECIDE NOT TO USE IT.
Updates

Thank you all so much for your designs. I will be providing feedback to ALL designers tomorrow. This weekend is a holiday weekend here in New Zealand and so no work for a few days. Thank-you again - I appreciate your time and creativity!

Industry/Entity Type

Camera

Font styles to use
Other font styles liked:
• Maven Pro - open to others

Requirements
Must have
• Clean design. Logo must be prominent for brand recognition. All contact information must be shown.
Nice to have
• Tagline - at least on reverse

```html
<!DOCTYPE html>
<html lang="en">
<head>
<meta charset="utf-8">
<title>Loomfield Goods Co. — Business Card</title>
<link rel="stylesheet" href="https://fonts.googleapis.com/css2?family=Maven+Pro:wght@400&family=Ubuntu:wght@300;400;700&display=swap">
<style>
  :root {
    --ink: #58524f;
    --orange: #ee6440;
    --olive: #d2c21c;
    --teal: #4fa69a;
    --pale-yellow: #f4efb4;
    --grey-dark: #5e5956;
    --grey-light: #f1f1f0;
    --mint: #e3ebe7;
  }
  html, body {
    margin: 0;
    padding: 0;
    width: 923px;
    height: 1200px;
    overflow: hidden;
    background: #ffffff;
  }
  .canvas {
    position: relative;
    width: 923px;
    height: 1200px;
  }
  .card {
    position: absolute;
    overflow: hidden;
  }
  .card--front { left: 0; top: 0; width: 910px; height: 563px; }
  .card--back { left: 13px; top: 635px; width: 910px; height: 565px; }
  .card__art {
    position: absolute;
    inset: 0;
    width: 100%;
    height: 100%;
  }
  .brand-name {
    position: absolute;
    margin: 0;
    font-family: "Maven Pro", sans-serif;
    font-weight: 400;
    color: var(--ink);
    white-space: nowrap;
  }
  .card--front .brand-name { left: 29px; top: 150px; font-size: 30px; }
  .card--back .brand-name { left: 0; width: 910px; text-align: center; top: 268px; font-size: 62px; }
  .holder-name {
    position: absolute;
    left: 483px;
    top: 126px;
    margin: 0;
    font-family: "Ubuntu", sans-serif;
    font-weight: 700;
    font-size: 41px;
    color: var(--ink);
    text-shadow: 0 0 8px rgba(255,255,255,0.7);
  }
  .contact-list {
    position: absolute;
    left: 412px;
    top: 264px;
    margin: 0;
    padding: 0;
    list-style: none;
  }
  .contact-list__item {
    display: flex;
    align-items: center;
    height: 45.8px;
    font-family: "Ubuntu", sans-serif;
    font-size: 25px;
    color: var(--ink);
  }
  .contact-list__icon { width: 37px; height: 37px; margin-right: 16px; flex: none; }
  .tagline {
    position: absolute;
    left: 0;
    width: 910px;
    top: 368px;
    margin: 0;
    text-align: center;
    font-family: "Ubuntu", sans-serif;
    font-weight: 300;
    font-size: 36px;
    letter-spacing: 1.5px;
    color: var(--ink);
  }
  .back-url {
    position: absolute;
    right: 45px;
    top: 482px;
    margin: 0;
    font-family: "Ubuntu", sans-serif;
    font-size: 38px;
    color: var(--ink);
  }
</style>
</head>
<body>
<main class="canvas">

  <section class="card card--front" aria-label="Card front">
    <svg class="card__art" viewBox="0 0 910 563" preserveAspectRatio="none" aria-hidden="true">
      <defs>
        <linearGradient id="front-yellow" x1="0" y1="0" x2="1" y2="0">
          <stop offset="0" stop-color="#ffffff"/>
          <stop offset="0.35" stop-color="var(--pale-yellow)"/>
          <stop offset="1" stop-color="var(--olive)"/>
        </linearGradient>
        <linearGradient id="front-grey" x1="0" y1="1" x2="1" y2="0">
          <stop offset="0" stop-color="#ffffff"/>
          <stop offset="0.45" stop-color="#dcdbda"/>
          <stop offset="1" stop-color="#8f8b88"/>
        </linearGradient>
        <linearGradient id="front-swoosh" x1="0" y1="1" x2="1" y2="0">
          <stop offset="0" stop-color="#ffffff" stop-opacity="0"/>
          <stop offset="0.5" stop-color="var(--grey-dark)" stop-opacity="0.6"/>
          <stop offset="1" stop-color="var(--grey-dark)"/>
        </linearGradient>
      </defs>
      <rect width="910" height="563" fill="url(#front-yellow)"/>
      <path d="M0,563 C150,300 450,90 910,0 L910,563 Z" fill="url(#front-grey)"/>
      <path d="M12,563 C170,320 470,120 910,20 L910,150 C620,170 300,300 80,563 Z" fill="url(#front-swoosh)" opacity="0.55"/>
      <path d="M0,560 C150,300 450,90 910,0" fill="none" stroke="var(--orange)" stroke-width="4"/>
      <path d="M6,560 C160,308 460,100 910,12" fill="none" stroke="var(--grey-dark)" stroke-width="4"/>
      <path d="M14,560 C170,316 470,112 910,26" fill="none" stroke="#ffffff" stroke-width="3"/>
      <circle cx="172" cy="96" r="44" fill="var(--orange)"/>
    </svg>

    <p class="brand-name">Loomfield Goods Co.</p>
    <h1 class="holder-name">Maren Oakley</h1>

    <ul class="contact-list">
      <li class="contact-list__item">
        <svg class="contact-list__icon" viewBox="0 0 36 36" aria-hidden="true"><circle cx="18" cy="18" r="17" fill="var(--orange)" stroke="#ffffff" stroke-width="1.5"/><path d="M12,10 l4,-1 2,5 -2.5,1.5 c1,2.5 2.5,4 5,5 l1.5,-2.5 5,2 -1,4 c-8,0 -14,-6 -14,-14 z" fill="#ffffff"/></svg>
        +64 (0) 3 555 0147
      </li>
      <li class="contact-list__item">
        <svg class="contact-list__icon" viewBox="0 0 36 36" aria-hidden="true"><circle cx="18" cy="18" r="17" fill="var(--olive)" stroke="#ffffff" stroke-width="1.5"/><rect x="13" y="8" width="10" height="20" rx="2" fill="none" stroke="#ffffff" stroke-width="2"/><rect x="15" y="11" width="6" height="5" fill="#ffffff"/></svg>
        +64 (0) 21 555 03926
      </li>
      <li class="contact-list__item">
        <svg class="contact-list__icon" viewBox="0 0 36 36" aria-hidden="true"><circle cx="18" cy="18" r="17" fill="var(--teal)" stroke="#ffffff" stroke-width="1.5"/><rect x="9" y="12" width="18" height="12" fill="#ffffff"/><path d="M9,12 l9,7 9,-7" fill="none" stroke="var(--teal)" stroke-width="1.5"/></svg>
        maren.oakley@loomfieldnz.example
      </li>
      <li class="contact-list__item">
        <svg class="contact-list__icon" viewBox="0 0 36 36" aria-hidden="true"><circle cx="18" cy="18" r="17" fill="var(--grey-dark)" stroke="#ffffff" stroke-width="1.5"/></svg>
        social.example/loomfield
      </li>
      <li class="contact-list__item">
        <svg class="contact-list__icon" viewBox="0 0 36 36" aria-hidden="true"><circle cx="18" cy="18" r="17" fill="var(--teal)" stroke="#ffffff" stroke-width="1.5"/><rect x="11" y="14" width="14" height="13" rx="1" fill="#ffffff"/><path d="M14,14 v-2 a4,4 0 0 1 8,0 v2" fill="none" stroke="#ffffff" stroke-width="1.5"/></svg>
        www.tindalerow.example
      </li>
      <li class="contact-list__item">
        <svg class="contact-list__icon" viewBox="0 0 36 36" aria-hidden="true"><circle cx="18" cy="18" r="17" fill="var(--orange)" stroke="#ffffff" stroke-width="1.5"/><g fill="none" stroke="#ffffff" stroke-width="1.3"><circle cx="18" cy="18" r="9"/><ellipse cx="18" cy="18" rx="4" ry="9"/><path d="M9,18 h18 M10.5,13.5 h15 M10.5,22.5 h15"/></g></svg>
        www.loomfieldnz.example
      </li>
    </ul>
  </section>

  <section class="card card--back" aria-label="Card back">
    <svg class="card__art" viewBox="0 0 910 565" preserveAspectRatio="none" aria-hidden="true">
      <defs>
        <linearGradient id="back-band-top" x1="0" y1="0" x2="1" y2="0">
          <stop offset="0" stop-color="#f9d6cc"/>
          <stop offset="1" stop-color="var(--orange)"/>
        </linearGradient>
        <linearGradient id="back-band-bottom" x1="0" y1="0" x2="1" y2="0">
          <stop offset="0" stop-color="#fdf3f0"/>
          <stop offset="1" stop-color="#f08f74"/>
        </linearGradient>
        <linearGradient id="back-panel" x1="0" y1="0" x2="1" y2="0">
          <stop offset="0" stop-color="#ffffff"/>
          <stop offset="1" stop-color="var(--mint)"/>
        </linearGradient>
      </defs>
      <rect x="0" y="0" width="910" height="100" fill="url(#back-band-top)"/>
      <rect x="0" y="100" width="910" height="9" fill="var(--grey-dark)"/>
      <rect x="0" y="109" width="910" height="347" fill="url(#back-panel)"/>
      <rect x="0" y="456" width="910" height="9" fill="var(--grey-dark)"/>
      <rect x="0" y="465" width="910" height="100" fill="url(#back-band-bottom)"/>
      <circle cx="455" cy="200" r="58" fill="var(--orange)"/>
    </svg>

    <p class="brand-name">Loomfield Goods Co.</p>
    <p class="tagline">HollowReed Ideas &amp; Hobby Materials</p>
    <p class="back-url">www.tindalerow.example</p>
  </section>

</main>
</body>
</html>
```